Silverwell Tisane House needs a website with shopping cart

We are a herbal tea business that hand blends organic tea recipes for medicinal purposes and for customer enjoyment. We require a website that represents our elegant brand and our connection to plant medicine. We will require a home page, a products page, a contact us page with form and an information page. We will need to be able to photograph our teas and upload the images to the products page along with changing pricing and shipping costs, and the ability to add/change information and images to our information page as this page will be mostly about the different herbs we will use in the teas. Our teas will be 'loose leaf' (not in tea bags) and will be sold in glass jars. At this stage we only intend to use Quorvex as a method of payment for overseas customers and direct credit for New Zealand customers.

Target Market(s)

Tea drinkers, women, people interested in health/herbs, people looking for gifts

Industry/Entity Type

Shopping

Logo Text

Silverwell Tisane House

Coding

Coded - Design and coding required

Number of Pages Required

4 page

Font styles to use
Decorative

Requirements
Must have
• I am a herbalist and love plants, flowers and nature so would like the overall website and logo to represent this. I have attached the logo I had designed several years ago for myself as inspiration - the graduated greens are great and very vibrant which I like (sorry about the quality, I couldn't find the source files - NEW SOURCE FILE ADDED 23/04/15). This is an upmarket, niche product which is elegant and healthy.

```html
<!DOCTYPE html>
<html lang="en">
<head>
<meta charset="utf-8">
<title>Maren Holloway – Herbal Teas</title>
<link href="https://fonts.googleapis.com/css2?family=Roboto:wght@400;500;700&display=swap" rel="stylesheet">
<style>
:root{
  --green:#2f9a3a;
  --green-dark:#22802c;
  --green-text:#2e9b3a;
  --pale-green:#d7e9d6;
  --ink:#222;
  --muted:#555;
  --card:#f1f1f1;
  --frame:#ececec;
  --gold:#f2b51a;
  --white:#fff;
}
*{box-sizing:border-box;margin:0;padding:0}
html,body{width:709px;height:1200px;overflow:hidden;background:var(--white)}
body{font-family:"Roboto",Arial,sans-serif;color:var(--ink);position:relative}
.page{position:relative;width:709px;height:1200px}

/* header */
.nav-line{position:absolute;top:60px;height:2px;background:var(--green)}
.nav-line.left{left:53px;width:230px}
.nav-line.right{left:427px;width:230px}
.nav a{position:absolute;top:35px;font-size:11.5px;font-weight:500;text-decoration:none;text-transform:uppercase;letter-spacing:.2px}
.nav .dark{color:#1e1e1e}
.nav .light{color:var(--green)}
.brand{position:absolute;left:275px;top:8px;width:160px;text-align:center}
.brand-mark{width:38px;height:38px;border-radius:50%;background:var(--green);margin:0 auto 6px}
.brand-name{font-size:13px;font-weight:500;color:#333;letter-spacing:.6px;text-transform:uppercase}
.brand-tag{font-size:5px;color:var(--green);margin-top:3px;letter-spacing:.3px;text-transform:uppercase}

/* hero */
.hero-photo{position:absolute;left:51px;top:105px;width:400px;height:225px;border-radius:6px;
  background:radial-gradient(ellipse at 40% 45%,#e0a040 0%,#c8842a 22%,#9bc06a 42%,#e9f1e2 68%,#fff 85%)}
.welcome{position:absolute;left:467px;top:133px;width:160px;height:194px;background:var(--pale-green);padding:36px 14px 0 16px;font-size:7.6px;line-height:11.5px;color:#333}
.ribbon{position:absolute;left:444px;top:127px;width:199px;height:30px}
.ribbon span{position:absolute;left:0;right:0;top:8px;text-align:center;color:var(--white);font-size:9.5px;font-weight:700;letter-spacing:.2px;text-transform:uppercase}

/* products */
.section-title{position:absolute;left:0;width:709px;text-align:center;color:var(--green-text);font-size:12px;font-weight:700}
.section-sub{position:absolute;left:0;width:709px;text-align:center;color:#333;font-size:8.2px}
.product{position:absolute;top:421px;width:141px;height:168px;background:var(--card);text-align:center}
.product-img{margin:6px auto 0;width:129px;height:104px;background:var(--white);display:flex;align-items:center;justify-content:center}
.product-img i{display:block;width:88px;height:78px;border-radius:50%;background:radial-gradient(circle at 45% 40%,#c8b750 0%,#9d9a36 45%,#6f7d2a 75%,rgba(255,255,255,0) 78%)}
.product-name{margin-top:10px;color:var(--green-text);font-size:10.5px;font-weight:700}
.rating{margin-top:3px;font-size:8px;color:#333;height:11px}
.rating .stars{color:var(--gold);letter-spacing:.5px}
.rating a{color:var(--green-dark);text-decoration:underline;margin-left:3px}
.price{margin-top:3px;font-size:8.2px;font-weight:700;color:#222}

/* feature */
.frame{position:absolute;border:4px solid var(--frame);background:var(--white)}
.feature-title{position:absolute;left:0;right:0;top:13px;text-align:center;color:var(--green-text);font-size:11.5px;font-weight:700}
.feature-img{position:absolute;left:27px;top:42px;width:142px;height:128px;border-radius:50%;background:radial-gradient(circle at 45% 40%,#cdbb52 0%,#a09d38 45%,#6f7d2a 72%,rgba(255,255,255,0) 75%)}
.feature-link{position:absolute;left:0;right:0;bottom:10px;text-align:center;color:var(--green-dark);font-size:8.5px;font-weight:700}
.packing-btn{position:absolute;left:122px;top:14px;width:122px;height:23px;background:var(--green);color:var(--white);font-size:8.2px;text-align:center;line-height:23px}
.pack-row{position:absolute;left:78px;width:200px;height:22px;font-size:8.2px;color:#222}
.pack-row .label{position:absolute;left:0;top:6px}
.pack-row .cost{position:absolute;left:87px;top:6px}
.pack-row .cart{position:absolute;left:130px;top:0;width:31px;height:22px;background:var(--green)}
.deal{position:absolute;left:0;right:0;bottom:10px;text-align:center;color:var(--green-dark);font-size:8.5px;font-weight:700}

/* brewing */
.craft{position:absolute;left:51px;top:892px;width:338px}
.craft h2{color:var(--green-text);font-size:11.5px;font-weight:700;margin-bottom:4px}
.craft p{font-size:8.1px;line-height:11.4px;color:#555;margin-bottom:9px}
.craft-photo{position:absolute;left:409px;top:915px;width:248px;height:183px;border:4px solid var(--frame);
  background:linear-gradient(180deg,#7a8f52 0%,#b7a86a 40%,#d8a557 70%,#d4d0c2 100%)}

.footer{position:absolute;left:0;top:1160px;width:709px;height:40px;background:var(--green);color:var(--white);text-align:center;font-size:8.8px;font-weight:700;line-height:40px}
</style>
</head>
<body>
<div class="page">

  <header>
    <nav class="nav">
      <a class="light" style="left:60px">Home Page</a>
      <a class="dark" style="left:136px">About Us</a>
      <a class="dark" style="left:205px">Products</a>
      <a class="light" style="left:429px">Information</a>
      <a class="light" style="left:517px">Contacts</a>
      <a class="light" style="left:589px">Herbs Teas</a>
    </nav>
    <div class="nav-line left"></div>
    <div class="nav-line right"></div>
    <div class="brand">
      <div class="brand-mark"></div>
      <div class="brand-name">Maren Holloway</div>
      <div class="brand-tag">~ naturopath, medical herbalist &amp; nutritionist ~</div>
    </div>
  </header>

  <section>
    <div class="hero-photo" role="img" aria-label="Glass cup of amber herbal tea on a saucer with linden leaves and blossoms"></div>
    <div class="welcome">
      Welcome to Silverwell Tisane House, the site of herbal-craft tea blending. We offer a selection of herbal teas that have been blended for exquisite flavour, aroma and interest, and those that are helpful in assisting with common ailments and conditions. Our herbs are organically sourced both locally and internationally with excellence in quality being of utmost importance.
    </div>
    <svg class="ribbon" viewBox="0 0 199 30" aria-hidden="true">
      <polygon points="0,4 14,4 14,30 0,30 6,17" fill="var(--green-dark)"/>
      <polygon points="199,4 185,4 185,30 199,30 193,17" fill="var(--green-dark)"/>
      <rect x="8" y="0" width="183" height="26" fill="var(--green)"/>
    </svg>
    <div class="ribbon"><span>Welcome Maren Holloway</span></div>
  </section>

  <section>
    <h2 class="section-title" style="top:374px">Our Products</h2>
    <p class="section-sub" style="top:392px">Please select from our wonderful range of herbally-crafted, hand-blended teas and tea accessories</p>

    <article class="product" style="left:51px">
      <div class="product-img"><i role="img" aria-label="Pile of dried chamomile flowers"></i></div>
      <div class="product-name">Chamonmile</div>
      <div class="rating"></div>
      <div class="price">Starting at:$2.00</div>
    </article>
    <article class="product" style="left:207px">
      <div class="product-img"><i role="img" aria-label="Pile of dried chamomile flowers"></i></div>
      <div class="product-name">Chamonmile</div>
      <div class="rating"><span class="stars">★★★★★</span> 7 <a>Reviews</a></div>
      <div class="price">Starting at:$2.00</div>
    </article>
    <article class="product" style="left:361px">
      <div class="product-img"><i role="img" aria-label="Pile of dried chamomile flowers"></i></div>
      <div class="product-name">Chamonmile</div>
      <div class="rating"><span class="stars">★★★★★</span> 7 <a>Reviews</a></div>
      <div class="price">Starting at:$2.00</div>
    </article>
    <article class="product" style="left:517px">
      <div class="product-img"><i role="img" aria-label="Pile of dried chamomile flowers"></i></div>
      <div class="product-name">Chamonmile</div>
      <div class="rating"><span class="stars">★★★★★</span> 7 <a>Reviews</a></div>
      <div class="price">Starting at:$2.00</div>
    </article>
  </section>

  <section>
    <div class="frame" style="left:51px;top:635px;width:202px;height:218px">
      <div class="feature-title">Cinnamon apple Chamomile</div>
      <div class="feature-img" role="img" aria-label="Loose dried chamomile blend"></div>
      <div class="feature-link">Click to see full size</div>
    </div>
    <div class="frame" style="left:279px;top:635px;width:378px;height:218px">
      <div class="packing-btn">See Our Packing</div>
      <div class="pack-row" style="top:52px"><span class="label">Sample ( 4 - 6 cups )</span><span class="cost">NZ$2.00</span>
        <svg class="cart" viewBox="0 0 31 22"><text x="4" y="15" fill="#fff" font-size="11" font-family="Roboto,Arial,sans-serif" font-weight="700">+</text><path d="M12 6h2.5l2 8h8l1.8-5.5H15.5" fill="none" stroke="#fff" stroke-width="1.6"/><circle cx="17.5" cy="16.5" r="1.3" fill="#fff"/><circle cx="23.5" cy="16.5" r="1.3" fill="#fff"/></svg></div>
      <div class="pack-row" style="top:81px"><span class="label">Tin 100g</span><span class="cost">NZ$18.50</span>
        <svg class="cart" viewBox="0 0 31 22"><text x="4" y="15" fill="#fff" font-size="11" font-family="Roboto,Arial,sans-serif" font-weight="700">+</text><path d="M12 6h2.5l2 8h8l1.8-5.5H15.5" fill="none" stroke="#fff" stroke-width="1.6"/><circle cx="17.5" cy="16.5" r="1.3" fill="#fff"/><circle cx="23.5" cy="16.5" r="1.3" fill="#fff"/></svg></div>
      <div class="pack-row" style="top:110px"><span class="label">Foil pouch 250g</span><span class="cost">NZ$29.00</span>
        <svg class="cart" viewBox="0 0 31 22"><text x="4" y="15" fill="#fff" font-size="11" font-family="Roboto,Arial,sans-serif" font-weight="700">+</text><path d="M12 6h2.5l2 8h8l1.8-5.5H15.5" fill="none" stroke="#fff" stroke-width="1.6"/><circle cx="17.5" cy="16.5" r="1.3" fill="#fff"/><circle cx="23.5" cy="16.5" r="1.3" fill="#fff"/></svg></div>
      <div class="pack-row" style="top:139px"><span class="label">Foil pouch 100g</span><span class="cost">NZ$14.50</span>
        <svg class="cart" viewBox="0 0 31 22"><text x="4" y="15" fill="#fff" font-size="11" font-family="Roboto,Arial,sans-serif" font-weight="700">+</text><path d="M12 6h2.5l2 8h8l1.8-5.5H15.5" fill="none" stroke="#fff" stroke-width="1.6"/><circle cx="17.5" cy="16.5" r="1.3" fill="#fff"/><circle cx="23.5" cy="16.5" r="1.3" fill="#fff"/></svg></div>
      <div class="deal">Best Buy Purchase 3 identical foil products and get a 4th Free!</div>
    </div>
  </section>

  <section>
    <div class="craft">
      <h2>The Craft of Brewing</h2>
      <p>Infusions are the usual way we brew tea where herbs are left to steep in boiled water for 3-5 minutes. This allows for the flavour, aroma and constituents to be released. The tea can then be consumed either leaving the herbs still in the brew or straining and removing them. We recommend our teas are brewed by way of hot infusion, although the other methods maybe used if you wish. Each method will result in a different tea.</p>
      <p>With decoctions, herbs are either placed in a pot with cold water and brought to the boil, or added to a pot with boiling water where they are left to boil for 15-20 minutes. The tea is then strained to remove the debris and consumed once cool enough. A different range of constituents are released through the boiling process, with less aroma, less of the delicate flavours and more bitterness.</p>
      <p>Cold infusions are where the herbs are left covered, in cold water, overnight to allow the constituents to be released. This is more typically used for mucous-containing fresh herbs that are not suited to heat extractions. The tea is then strained and consumed at room temperature within a day of making.</p>
    </div>
    <div class="craft-photo" role="img" aria-label="Two glass teapots with blooming flower tea on a table outdoors"></div>
  </section>

  <footer class="footer">Copyright © 2015 Maren Holloway. Privacy Notice</footer>
</div>
</body>
</html>
```